Funky new Serviced Apartment Company needs a website + logo

Bright Harbor Serviced Lodging is a new company aiming to attract customers who need temporary accommodation (2 days to 6 months) in city locations.

Our customers make considerable savings on longer stays compared to hotels, and have all the creature comforts of home including super-fast WIFI, comfy beds, full kitchen and modern, yet comfortable, furniture.

Another key feature of the design is a page to attract "Partners" who "Work with Us" by allowing us to manage their properties and becoming part of our network of accommodation units. I have include a brochure from one of our competitors, and a video can be found here: http://lnkshort.example/clipz-7 - both can be used as I have permission.

The website design should work on all devices and screen sizes, and lend itself to a mobile app.

We would like to see website designs that are modern and simple, with a strong brand logo. The final design should communicate "Home From Home" and aim to attract professionals away from home on business for long periods of time.

Target Market(s)

Professional People working away from home for extended periods of time

Industry/Entity Type

Accommodation

Contact Information for Business Card

Name, Title, Phone Number, Email
Malcolm Ostby, Owner, 07831 562087, malcolm.ostby@brightharborsl.co.uk

Logo Text

Bright Harbor Service Lodging (Serviced Accommodation optional)

Coding

Coded - Design and coding required

Number of Pages Required

3 page

Font styles to use
Sans Serif

Requirements
Must have
• A 3 page website: Home, Partners, Contact Us
• Home page should have an area to list current apartment units, the user should be able to select a location and filter the list based on price and number of people.
• Partners page should inspire a "Work with us" call to action.
• The design should work with all screen sizes and devices.
• The design should say friendly and professional
Nice to have
• A simple logo, perhaps a smiling face made up using letters 'W' and 'H'.
• A neutral color scheme
Should not have
• No garish or vivid color scheme

```html
<!DOCTYPE html>
<html lang="en">
<head>
<meta charset="utf-8">
<title>Bright Harbor Serviced Lodging</title>
<link href="https://fonts.googleapis.com/css2?family=Lora:wght@400;700&family=Open+Sans:wght@400;600;700&display=swap" rel="stylesheet">
<style>
:root{
  --gold:#c7821c;
  --gold-dark:#a9670f;
  --gold-light:#dba040;
  --ink:#2b2b2b;
  --text:#666;
  --muted:#999;
  --line:#e4e4e4;
  --bg-soft:#f5f5f5;
  --dark:#24282c;
  --white:#fff;
}
*{box-sizing:border-box;margin:0;padding:0}
html,body{width:1200px;height:4063px;overflow:hidden}
body{font-family:"Open Sans",Arial,sans-serif;color:var(--text);background:var(--white);position:relative}
.section-title{font-family:"Lora",Georgia,serif;font-size:32px;color:var(--ink);text-align:center;font-weight:400}
.section-sub{font-family:"Lora",Georgia,serif;font-style:italic;font-size:12px;color:#777;text-align:center;margin-top:8px}
.btn{display:inline-block;background:linear-gradient(var(--gold-light),var(--gold-dark));color:#fff;font-family:"Lora",Georgia,serif;font-weight:700;font-size:14px;border-radius:3px;text-align:center}

/* top bar */
.topbar{height:43px;background:#f7f7f7;border-bottom:1px solid #ececec;display:flex;align-items:center;justify-content:space-between;padding:0 133px;font-size:10px;color:#777}
.topbar .left{display:flex;gap:26px;align-items:center}
.topbar .left span{display:flex;align-items:center;gap:6px}
.topbar .gold{color:var(--gold)}
.topbar .follow{display:flex;align-items:center;gap:20px}
.topbar .dot{width:8px;height:8px;border-radius:50%;background:var(--gold)}

/* header */
.header{height:120px;display:flex;align-items:center;justify-content:space-between;padding:0 133px}
.brand{display:flex;align-items:center;gap:12px}
.brand-mark{width:54px;height:54px;border-radius:50%;background:var(--gold)}
.brand-name{font-family:"Lora",Georgia,serif;font-weight:700;font-size:19px;line-height:1.2;color:var(--ink);width:240px}
.nav{display:flex;gap:32px;align-items:center;font-family:"Lora",Georgia,serif;font-size:14px;color:#333}
.nav .active{color:var(--gold)}

/* hero */
.hero{position:relative;height:582px;background:linear-gradient(100deg,#5a3b22 0%,#8a6440 30%,#b0896a 55%,#7d5534 80%,#4a3220 100%)}
.hero::after{content:"";position:absolute;inset:0;background:rgba(0,0,0,.18)}
.hero-text{position:absolute;top:118px;left:0;right:0;text-align:center;color:#fff;z-index:1}
.hero-text .small{font-family:"Lora",Georgia,serif;font-size:34px}
.hero-text .big{font-family:"Lora",Georgia,serif;font-size:78px;font-weight:700;letter-spacing:2px;line-height:1.1}
.hero-dots{position:absolute;top:290px;left:0;right:0;display:flex;justify-content:center;gap:12px;z-index:1}
.hero-dots i{width:14px;height:14px;border-radius:50%;border:2px solid #fff}
.hero-dots i.on{background:var(--gold);border-color:#f3d08a}

/* search */
.search{position:absolute;top:650px;left:133px;width:934px;height:195px;background:#fff;box-shadow:0 3px 14px rgba(0,0,0,.2);padding:18px 24px;z-index:2}
.search h3{font-family:"Lora",Georgia,serif;color:var(--gold);font-size:21px;font-weight:700}
.search .filter{position:absolute;top:22px;right:24px}
.search .labels,.search .fields{display:grid;grid-template-columns:206px 254px 126px 126px 123px;gap:0 10px}
.search .labels{font-size:13px;color:#444;margin-top:6px}
.field{height:34px;border:1px solid #ddd;font-size:10px;color:#999;display:flex;align-items:center;justify-content:space-between;padding:0 9px;margin-top:6px}
.field-pair{display:flex;gap:10px}
.field-pair .field{flex:1}
.search .btn{position:absolute;right:24px;bottom:24px;width:155px;height:34px;line-height:34px;font-size:14px}

/* apartments */
.apartments-wrap{position:absolute;top:905px;left:0;right:0}
.cards{display:flex;gap:31px;justify-content:center;margin-top:40px}
.apt{width:291px;height:287px;background:#fff;box-shadow:0 1px 8px rgba(0,0,0,.15);text-align:center}
.apt .photo{height:152px;position:relative}
.apt .price{position:absolute;right:0;top:52px;background:var(--gold);color:#fff;font-family:"Lora",Georgia,serif;font-weight:700;font-size:15px;padding:8px 12px}
.apt h4{font-family:"Lora",Georgia,serif;font-size:15px;color:var(--ink);margin-top:20px}
.apt p{font-size:10.5px;line-height:1.6;color:#888;margin:8px 30px 0}
.apt a{display:block;color:var(--gold);font-size:10.5px;text-decoration:underline;margin-top:6px}

/* work with us */
.work{position:absolute;top:1371px;left:0;width:1200px;height:363px;background:linear-gradient(180deg,#2d3237 0%,#1f2327 60%,#2a2f33 100%);text-align:center;color:#ddd}
.work .section-title{color:#fff;margin-top:90px}
.work p{font-size:11px;line-height:1.9;width:660px;margin:14px auto 0}
.work form{display:flex;justify-content:center;gap:8px;margin-top:24px}
.work .email{width:415px;height:40px;background:#fff;border-radius:2px;font-size:11px;color:#999;text-align:left;padding:12px 14px}
.work .btn{width:133px;height:40px;line-height:40px;display:flex;align-items:center;justify-content:center;gap:8px}

/* testimonials */
.testimonials{position:absolute;top:1734px;left:0;width:1200px;height:569px;background:linear-gradient(90deg,#f1f1f1,#fafafa 50%,#ececec)}
.testimonials .section-title{margin-top:66px}
.tcards{display:flex;justify-content:center;gap:31px;margin-top:24px}
.tcard{width:291px;height:336px;background:#fff;box-shadow:0 1px 8px rgba(0,0,0,.15);text-align:center;padding-top:30px}
.stars{display:flex;justify-content:center;gap:5px}
.tcard q{display:block;font-size:10.5px;line-height:1.7;color:#555;margin:16px 26px 0;quotes:none}
.tcard .more{font-size:10px;color:var(--muted);margin-top:8px}
.avatar{width:54px;height:54px;border-radius:50%;margin:16px auto 0;background:linear-gradient(#e2c6b3,#b88c74)}
.tcard h5{font-family:"Lora",Georgia,serif;font-size:16px;color:var(--ink);font-weight:400;margin-top:14px}
.tcard .date{font-size:11px;color:#777;margin-top:4px}

/* blog */
.blog{position:absolute;top:2303px;left:0;width:1200px;height:528px;background:#fff}
.blog .section-title{margin-top:60px}
.posts{display:flex;justify-content:center;gap:27px;margin-top:40px}
.post{width:463px;height:211px;background:#fff;box-shadow:0 1px 8px rgba(0,0,0,.15);display:flex;padding:8px}
.post .photo{width:206px;height:195px}
.post .body{padding:22px 0 0 26px;flex:1}
.post h4{font-family:"Lora",Georgia,serif;font-size:15px;font-weight:400;color:var(--ink);line-height:1.6}
.post p{font-size:10.5px;line-height:1.7;color:#888;margin-top:10px}
.post .when{font-size:10px;color:var(--gold);margin-top:12px;display:flex;gap:6px;align-items:center;font-style:italic}
.blog .btn{position:absolute;left:520px;top:409px;width:157px;height:40px;line-height:40px}

/* gallery */
.gallery{position:absolute;top:2831px;left:0;width:1200px;height:739px;background:var(--bg-soft)}
.gallery .section-title{margin-top:60px}
.tile{position:absolute;border:6px solid #fff;border-radius:18px;transform:rotate(45deg);box-shadow:0 2px 10px rgba(0,0,0,.2)}
.tile.s{width:150px;height:150px}
.tile.l{width:234px;height:234px}
.gallery .btn{position:absolute;left:525px;top:615px;width:150px;height:43px;line-height:43px}

/* mailing */
.mailing{position:absolute;top:3570px;left:0;width:1200px;height:209px;background:linear-gradient(90deg,#2a2d31,#1d2024 60%,#2b2f33);display:flex;align-items:center;padding:0 160px;color:#fff}
.mailing .plane{margin-right:26px}
.mailing h3{font-family:"Lora",Georgia,serif;font-style:italic;font-size:25px;font-weight:700}
.mailing p{font-size:12px;color:#ccc;margin-top:4px}
.mailing form{margin-left:auto;display:flex}
.mailing .email{width:357px;height:40px;background:#fff;color:#999;font-size:11px;padding:12px 14px}
.mailing .btn{width:121px;height:40px;line-height:40px;border-radius:0}

/* contact */
.contact{position:absolute;top:3779px;left:0;width:1200px;height:284px;background:#fff}
.contact .section-title{margin-top:30px}
.contact-row{display:flex;align-items:flex-start;padding:0 133px;margin-top:24px}
.contact-row .brand{margin-top:-4px;width:372px}
.cols{display:flex;font-size:9.5px;color:#555;text-transform:uppercase;line-height:2.2;border-top:1px solid var(--line);padding-top:4px}
.cols ul{list-style:none;width:150px}
.cols ul:last-child{width:200px}
.copyright{position:absolute;top:222px;left:133px;right:133px;border-top:1px solid var(--line);text-align:center;font-size:9px;color:#666;padding-top:14px;text-transform:uppercase}
</style>
</head>
<body>

<div class="topbar">
  <div class="left">
    <span><svg width="8" height="12" viewBox="0 0 8 12"><rect x="0.5" y="0.5" width="7" height="11" rx="1.5" fill="none" stroke="#c7821c"/></svg>Call us : <b class="gold">1.800.555.0142</b></span>
    <span><svg width="9" height="11" viewBox="0 0 9 11"><rect x="0" y="4.5" width="9" height="6.5" fill="#c7821c"/><path d="M2 4.5V3a2.5 2.5 0 015 0v1.5" fill="none" stroke="#c7821c"/></svg>Login / Make an Enquiry</span>
  </div>
  <div class="follow">Follow us : <i class="dot"></i><i class="dot"></i><i class="dot"></i><i class="dot"></i><i class="dot"></i></div>
</div>

<header class="header">
  <div class="brand"><span class="brand-mark"></span><span class="brand-name">Bright Harbor Serviced Lodging</span></div>
  <nav class="nav">
    <span class="active">Home</span><span>About us</span><span>Services</span><span>Testimonials</span><span>Gallery</span><span>Contact us</span>
    <svg width="14" height="14" viewBox="0 0 14 14"><circle cx="6" cy="6" r="4.5" fill="none" stroke="#c7821c" stroke-width="1.5"/><path d="M9.5 9.5L13 13" stroke="#c7821c" stroke-width="1.5"/></svg>
  </nav>
</header>

<section class="hero" role="img" aria-label="Photo of a warm, modern serviced apartment bedroom">
  <div class="hero-text"><div class="small">Bright Harbor Serviced</div><div class="big">LODGING</div></div>
  <div class="hero-dots"><i class="on"></i><i></i><i></i></div>
</section>

<form class="search">
  <h3>Accommodation</h3>
  <svg class="filter" width="16" height="16" viewBox="0 0 16 16"><path d="M1 1h14l-5.5 7v6l-3-2V8z" fill="#333"/></svg>
  <div class="labels"><span>Location</span><span>Date</span><span>Adults</span><span>Children</span><span>Price</span></div>
  <div class="fields">
    <div class="field">Select a Location <svg width="11" height="11" viewBox="0 0 11 11"><circle cx="5.5" cy="5.5" r="4.5" fill="none" stroke="#777"/><circle cx="5.5" cy="5.5" r="1.5" fill="#777"/></svg></div>
    <div class="field-pair">
      <div class="field">Arrival date <svg width="10" height="10" viewBox="0 0 10 10"><rect x=".5" y="1.5" width="9" height="8" fill="none" stroke="#777"/><path d="M.5 4h9" stroke="#777"/></svg></div>
      <div class="field">Departure date <svg width="10" height="10" viewBox="0 0 10 10"><rect x=".5" y="1.5" width="9" height="8" fill="none" stroke="#777"/><path d="M.5 4h9" stroke="#777"/></svg></div>
    </div>
    <div class="field">1+ <span>&#8597;</span></div>
    <div class="field">1+ <span>&#8597;</span></div>
    <div class="field">30,000 <span>$</span></div>
  </div>
  <span class="btn">Check Availability</span>
</form>

<div class="apartments-wrap">
  <h2 class="section-title">Available Apartments</h2>
  <p class="section-sub">Consectetur adipiscing elit, sed do eiusmod tempor incididunt ut labore et dolore magna aliqua</p>
  <div class="cards">
    <article class="apt">
      <div class="photo" role="img" aria-label="Photo of an apartment bedroom" style="background:linear-gradient(120deg,#7a5236,#c79a72 50%,#8a6142)"><span class="price">$32.99</span></div>
      <h4>Eiusmod Tempor</h4>
      <p>Aliquip ex ea commodo consequat. Duis dolor in reprehenderit...</p>
      <a>View More Details</a>
    </article>
    <article class="apt">
      <div class="photo" role="img" aria-label="Photo of an apartment living area" style="background:linear-gradient(120deg,#6d6a66,#c9c4bc 50%,#7f7a73)"><span class="price">$23.99</span></div>
      <h4>Eiusmod Tempor</h4>
      <p>Aliquip ex ea commodo consequat. Duis dolor in reprehenderit...</p>
      <a>View More Details</a>
    </article>
    <article class="apt">
      <div class="photo" role="img" aria-label="Photo of a bright open-plan lounge" style="background:linear-gradient(120deg,#8fa0ad,#e4e8ea 50%,#a0a9b0)"><span class="price">$18.99</span></div>
      <h4>Eiusmod Tempor</h4>
      <p>Aliquip ex ea commodo consequat. Duis dolor in reprehenderit...</p>
      <a>View More Details</a>
    </article>
  </div>
</div>

<section class="work" role="img" aria-label="Dark city skyline at night behind the call to action">
  <h2 class="section-title">Work With Us</h2>
  <p>Sed ut perspiciatis unde omnis iste natus error sit voluptat laudantium, totam rem aperiam, eaque ipsa quae ab illo inventore veritatis aliquip ex ea commodo et quasi architecto beatae vitae dicta sunt explicabo.</p>
  <form><div class="email">Email Address</div><span class="btn">MAIL US <svg width="11" height="11" viewBox="0 0 11 11"><circle cx="5.5" cy="5.5" r="5.5" fill="#fff"/><path d="M4.5 3l2.5 2.5L4.5 8" stroke="#c7821c" fill="none" stroke-width="1.4"/></svg></span></form>
</section>

<section class="testimonials">
  <h2 class="section-title">Testimonials</h2>
  <p class="section-sub">Consectetur adipiscing elit, sed do eiusmod tempor incididunt</p>
  <div class="tcards">
    <article class="tcard">
      <div class="stars"><svg width="76" height="12" viewBox="0 0 76 12"><g fill="#c7821c"><path id="st" d="M6 0l1.8 3.9 4.2.4-3.2 2.8 1 4.1L6 9.1 2.2 11.2l1-4.1L0 4.3l4.2-.4z"/><use href="#st" x="16"/><use href="#st" x="32"/><use href="#st" x="48"/><use href="#st" x="64"/></g></svg></div>
      <q>"Lorem Ipsum is simply dummy text of the printing and typesetting industry. Lorem Ipsum has been the industry's standard dummy text"</q>
      <div class="more">Read more</div>
      <div class="avatar" role="img" aria-label="Guest portrait"></div>
      <h5>Harborhal Utrecht</h5>
      <div class="date">30 September and 1 October 2017</div>
    </article>
    <article class="tcard">
      <div class="stars"><svg width="76" height="12" viewBox="0 0 76 12"><g fill="#c7821c"><use href="#st"/><use href="#st" x="16"/><use href="#st" x="32"/><use href="#st" x="48"/><use href="#st" x="64"/></g></svg></div>
      <q>"Lorem Ipsum is simply dummy text of the printing and typesetting industry. Lorem Ipsum has been the industry's standard dummy text"</q>
      <div class="more">Read more</div>
      <div class="avatar" role="img" aria-label="Guest portrait" style="background:linear-gradient(#d9b59c,#8f6a55)"></div>
      <h5>Parkzaal Breda</h5>
      <div class="date">21 and 22 October 2017</div>
    </article>
    <article class="tcard">
      <div class="stars"><svg width="76" height="12" viewBox="0 0 76 12"><g fill="#c7821c"><use href="#st"/><use href="#st" x="16"/><use href="#st" x="32"/><use href="#st" x="48"/><use href="#st" x="64"/></g></svg></div>
      <q>"Lorem Ipsum is simply dummy text of the printing and typesetting industry. Lorem Ipsum has been the industry's standard dummy text"</q>
      <div class="more">Read more</div>
      <div class="avatar" role="img" aria-label="Guest portrait" style="background:linear-gradient(#3a3330,#c9a58e)"></div>
      <h5>Lichthal Eindhoven</h5>
      <div class="date">20 and 21 January 2018</div>
    </article>
  </div>
</section>

<section class="blog">
  <h2 class="section-title">Blog</h2>
  <p class="section-sub">Consectetur adipiscing elit, sed do eiusmod tempor incididunt ut labore et dolore magna aliqua</p>
  <div class="posts">
    <article class="post">
      <div class="photo" role="img" aria-label="Photo of a hotel room with tall windows" style="background:linear-gradient(135deg,#5a3d27,#a98358 50%,#6b4a30)"></div>
      <div class="body">
        <h4>Tempor incididunt labo<br>Dolore magna</h4>
        <p>Liquip ex ea commodo quat. Duis aute irure dolor in reprehender in voluptate velit esse...</p>
        <div class="when"><svg width="10" height="10" viewBox="0 0 10 10"><rect x=".5" y="1.5" width="9" height="8" fill="none" stroke="#c7821c"/><path d="M.5 4h9" stroke="#c7821c"/></svg>Posted On 25 August 2017</div>
      </div>
    </article>
    <article class="post">
      <div class="photo" role="img" aria-label="Photo of a modern bedroom with warm lighting" style="background:linear-gradient(135deg,#3b2a20,#b36a2a 50%,#e2d6c8)"></div>
      <div class="body">
        <h4>Tempor incididunt labo<br>Dolore magna</h4>
        <p>Liquip ex ea commodo quat. Duis aute irure dolor in reprehender in voluptate velit esse...</p>
        <div class="when"><svg width="10" height="10" viewBox="0 0 10 10"><rect x=".5" y="1.5" width="9" height="8" fill="none" stroke="#c7821c"/><path d="M.5 4h9" stroke="#c7821c"/></svg>Posted On 25 August 2017</div>
      </div>
    </article>
  </div>
  <span class="btn">View All Blog Posts</span>
</section>

<section class="gallery">
  <h2 class="section-title">Photo Gallery</h2>
  <p class="section-sub">Consectetur adipiscing elit, sed do eiusmod tempor incididunt ut labore et dolore magna aliqua</p>
  <div class="tile s" role="img" aria-label="Photo of a bedroom" style="left:304px;top:182px;background:linear-gradient(135deg,#7a5a44,#d8c3ad)"></div>
  <div class="tile s" role="img" aria-label="Photo of a white dining corner" style="left:732px;top:182px;background:linear-gradient(135deg,#e8e4de,#b9a98f)"></div>
  <div class="tile l" role="img" aria-label="Photo of a grey living room" style="left:484px;top:276px;background:linear-gradient(135deg,#8d8c8a,#d6d3ce 55%,#5f5d5a)"></div>
  <div class="tile s" role="img" aria-label="Photo of a kitchen" style="left:304px;top:453px;background:linear-gradient(135deg,#5e5d5c,#cfcac2)"></div>
  <div class="tile s" role="img" aria-label="Photo of a white kitchen" style="left:732px;top:453px;background:linear-gradient(135deg,#dcdcdc,#8e8a84)"></div>
  <span class="btn">View All Photos</span>
</section>

<section class="mailing">
  <svg class="plane" width="60" height="50" viewBox="0 0 60 50"><path d="M2 22L58 2 46 46 30 32 22 46V30L50 8 18 28z" fill="none" stroke="#bbb" stroke-width="2" stroke-linejoin="round"/></svg>
  <div><h3>Join mailing list</h3><p>Subscribe to receive updates &amp; exclusive offers.</p></div>
  <form><div class="email">Enter your E - mail</div><span class="btn">SUBSCRIBE</span></form>
</section>

<footer class="contact">
  <h2 class="section-title">Contact Us</h2>
  <div class="contact-row">
    <div class="brand"><span class="brand-mark"></span><span class="brand-name">Bright Harbor Serviced Lodging</span></div>
    <div class="cols">
      <ul><li>Home</li><li>About us</li><li>Services</li></ul>
      <ul><li>Testimonials</li><li>Gallery</li><li>Contact us</li></ul>
      <ul><li>Terms &amp; conditions</li><li>Privacy policy</li></ul>
      <ul><li>Email : info@brightharborsl.com</li><li>Phone : 1.800.555.0199</li><li>Login / Make an enquiry</li></ul>
    </div>
  </div>
  <div class="copyright">Copyright © 2017, Bright Harbor Serviced Lodging | All rights reserved</div>
</footer>

</body>
</html>
```